Velora "Glass Tide" single cover

We need a cover for Velora's New upcoming single "Glass Tide"
We have posted some Pictures and logo that we want you to work With. We need you to get her to look good :).The title is "Glass Tide" and is "Velora feat. Dorvo mint rascal"
The songs is a little hiphop/RnB (Marla Q'ish).
You can choose what colour you want for the logo and overall. But we don't want it to be gloomy.
watch www.velora-music.example or www.facebook.com/veloramusic
This is a digital release so we need only front page 12x12cm
Updates
If anyone wants to remove the background from the pictures and be creative that is fine! :)
Industry/Entity Type
Digital
Colors
Designer to choose colors to be used in the design.
Look and feel
Each slider illustrates characteristics of the customer's brand and the style your logo design should communicate.

```html
<!DOCTYPE html>
<html lang="en">
<head>
<meta charset="utf-8">
<title>Velora – Glass Tide single cover</title>
<link rel="stylesheet" href="https://fonts.googleapis.com/css2?family=Poiret+One&display=swap">
<style>
  :root {
    --backdrop: #ebe9e4;
    --photo-deep: #2a1a4a;
    --photo-violet: #5a2f7e;
    --photo-magenta: #b0306e;
    --photo-orange: #e8782a;
    --photo-gold: #f4b04a;
    --logo-red: #c8102e;
    --feat-pink: #d8245a;
    --title-light: #ffd79a;
    --title-warm: #f08a2c;
    --title-edge: #7a2a10;
  }
  * { margin: 0; padding: 0; box-sizing: border-box; }
  html, body {
    width: 1200px;
    height: 900px;
    overflow: hidden;
    background: var(--backdrop);
  }
  .stage {
    position: relative;
    width: 1200px;
    height: 900px;
    display: flex;
    align-items: center;
    justify-content: center;
  }
  .cover {
    position: relative;
    width: 840px;
    height: 840px;
    overflow: hidden;
    font-family: "Poiret One", sans-serif;
  }
  .cover-photo {
    position: absolute;
    inset: 0;
    background:
      radial-gradient(ellipse 45% 55% at 30% 45%, var(--photo-orange) 0%, rgba(232,120,42,0) 70%),
      radial-gradient(ellipse 40% 35% at 85% 60%, var(--photo-gold) 0%, rgba(244,176,74,0) 70%),
      linear-gradient(160deg, var(--photo-magenta) 0%, var(--photo-violet) 45%, var(--photo-deep) 100%);
  }
  .artist-logo {
    position: absolute;
    top: 22px;
    right: 104px;
    font-size: 92px;
    line-height: 1;
    color: var(--logo-red);
    letter-spacing: 2px;
  }
  .featuring {
    position: absolute;
    top: 112px;
    right: 36px;
    font-size: 44px;
    line-height: 1;
    color: var(--feat-pink);
  }
  .title-block {
    position: absolute;
    left: 70px;
    top: 650px;
  }
  .title {
    font-size: 132px;
    line-height: 1;
    white-space: nowrap;
    background: linear-gradient(180deg, var(--title-light) 0%, var(--title-warm) 70%);
    -webkit-background-clip: text;
    background-clip: text;
    color: transparent;
    -webkit-text-stroke: 1.5px var(--title-edge);
  }
  .title-reflection {
    font-size: 132px;
    line-height: 1;
    white-space: nowrap;
    color: var(--title-warm);
    transform: scaleY(-1);
    opacity: 0.28;
    margin-top: -22px;
    -webkit-mask-image: linear-gradient(0deg, #000 0%, transparent 55%);
    mask-image: linear-gradient(0deg, #000 0%, transparent 55%);
  }
</style>
</head>
<body>
  <main class="stage">
    <section class="cover">
      <div class="cover-photo" role="img" aria-label="Photo of the singer with long curly red hair, seated against a brick wall in warm orange and violet light"></div>
      <div class="artist-logo">Velora</div>
      <div class="featuring">feat. Dorvo mint rascal</div>
      <div class="title-block">
        <h1 class="title">Glass Tide</h1>
        <div class="title-reflection" aria-hidden="true">Glass Tide</div>
      </div>
    </section>
  </main>
</body>
</html>
```